Website for The Velvet Pathfinder

We need an impressive e-commerce website for our newly launched business "The Velvet Pathfinder".
The Velvet Pathfinder searches store-front and online retailers for diamond engagement rings according to the client's specified requirements. We want to save people time by doing the shopping around for them.
We can relate to, and we love, www.corvaline.com
Like corvaline.com, we want to offer website visitors a quick run-down on how the process works, then offer them to elect a service package and pay for that package on the spot.
Content pages:
HOME
HOW IT WORKS
DIAMOND GALLERY
ABOUT
FAQs
CONTACT
Inclusions: Our logo and Facebook and Instagram buttons
We want to be able to easily edit this website, We want it to display well on iPhone and android, We want it to be clean and striking.
Like our logo, we want our website to embody elegant masculinity.
Target Market(s)
Men in market for diamond ring purchase $5k - $50k
Industry/Entity Type
Business
Number of Pages Required
5+ page
Font styles to use
Look and feel

```html
<!DOCTYPE html>
<html lang="en">
<head>
<meta charset="utf-8">
<title>The Velvet Pathfinder</title>
<link href="https://fonts.googleapis.com/css2?family=Cormorant+Garamond:wght@500;600;700&family=Open+Sans:wght@400;600&display=swap" rel="stylesheet">
<style>
:root{
  --ink:#333;
  --muted:#888;
  --line:#dcdcdc;
  --hero:#f0f0f0;
  --dark:#555;
  --bar:#4a4a4a;
  --white:#fff;
  --serif:"Cormorant Garamond", Georgia, serif;
  --sans:"Open Sans", Arial, sans-serif;
}
*{box-sizing:border-box;margin:0;padding:0}
html,body{width:711px;height:1200px;overflow:hidden;background:var(--white);font-family:var(--sans);color:var(--ink)}
.page{position:relative;width:711px;height:1200px}

/* header */
.site-header{height:46px;display:flex;align-items:center;padding:0 52px;justify-content:space-between}
.brand{display:flex;align-items:center;gap:6px}
.brand-dot{width:12px;height:12px;border-radius:50%;background:var(--dark)}
.brand-name{font-family:var(--serif);font-weight:700;font-size:10px;line-height:1.05;color:var(--ink)}
.main-nav{display:flex;align-items:center;gap:12px;font-size:6.5px;color:var(--ink)}
.main-nav .active{border:1px solid var(--line);padding:4px 8px}
.auth{display:flex;gap:6px;margin-left:10px}
.btn-sm{font-size:6px;padding:4px 9px;border:1px solid var(--dark);color:var(--dark)}
.btn-sm.fill{background:var(--dark);color:var(--white)}

/* hero */
.hero{position:relative;height:239px;background:var(--hero)}
.hero-text{position:absolute;left:52px;top:58px}
.hero-kicker{font-family:var(--serif);font-size:21px;font-weight:500;color:var(--dark)}
.hero-title{font-family:var(--serif);font-size:31px;font-weight:700;color:var(--ink);line-height:1.05}
.hero-sub{font-size:6.5px;color:var(--muted);margin-top:5px}
.btn-dark{display:inline-block;background:var(--dark);color:var(--white);font-size:7px;padding:6px 14px;margin-top:26px}
.hero-photo{position:absolute;left:440px;top:70px;width:170px;height:120px;border-radius:50%;
  background:radial-gradient(ellipse at center,#f6e6d8 0%,#d9b89a 40%,rgba(240,240,240,0) 72%)}
.hero-deco{position:absolute;right:20px;top:30px;width:60px;height:150px;
  background:linear-gradient(160deg,rgba(255,255,255,.9),rgba(255,255,255,0))}
.arrow{position:absolute;top:112px;font-size:16px;color:var(--ink)}
.arrow.left{left:12px}.arrow.right{right:12px}

/* section titles */
.section-title{font-family:var(--serif);font-size:19px;font-weight:600;text-align:center;color:var(--ink)}

/* process */
.process{position:absolute;top:300px;left:0;width:711px}
.steps{position:relative;margin-top:26px;height:110px}
.step-caption{position:absolute;top:86px;width:120px;text-align:center;font-size:6px;color:var(--muted)}
.step-caption b{display:block;font-weight:400;color:var(--ink);font-size:7px;margin-bottom:2px}

/* gallery */
.gallery{position:absolute;top:480px;left:52px;width:607px}
.gallery .section-title{margin-bottom:22px}
.grid{display:grid;grid-template-columns:300px 150px 150px;grid-template-rows:124px 124px;gap:4px}
.tile-photo{width:100%;height:100%}
.bracelet{grid-row:1/3;background:radial-gradient(ellipse at 50% 55%,#fafafa 0%,#d4d4d4 45%,#eeeeee 80%)}
.emerald{background:radial-gradient(circle at 50% 50%,#2f6f5a 0%,#7f8c86 28%,#e6e6e6 55%,#f3f3f3 80%)}
.gold{grid-column:2/4;background:radial-gradient(ellipse at 50% 50%,#c9ae6a 0%,#a8914f 22%,#ececec 50%,#f5f5f5 80%)}
.info-tile{background:#f3f3f3;display:flex;flex-direction:column;align-items:center;justify-content:center;text-align:center;padding:0 12px}
.info-tile h3{font-family:var(--serif);font-size:12px;font-weight:600}
.info-tile p{font-size:5.5px;color:var(--muted);line-height:1.5;margin:5px 0 7px}
.btn-line{font-size:6px;border:1px solid var(--muted);padding:4px 10px;color:var(--dark)}

/* packages */
.packages{position:absolute;top:842px;left:52px;width:607px;display:flex;gap:6px}
.pack-photo{width:280px;height:190px;background:radial-gradient(ellipse at 45% 50%,#cfd2d4 0%,#6c7074 30%,#e9e9e9 58%,#fff 85%)}
.pack-card{width:158px;height:190px;border:1px solid var(--line);text-align:center;padding-top:16px}
.pack-card h4{font-family:var(--serif);font-size:15px;font-weight:600}
.price{font-family:var(--serif);font-size:16px;font-weight:600;margin:8px 0 6px}
.price span{font-family:var(--sans);font-size:6px;color:var(--muted);font-weight:400}
.pack-card p{font-size:5.5px;color:var(--muted);line-height:1.6}
.pack-card .btn-dark{margin-top:10px;padding:5px 14px}
.pack-card .btn-line{display:inline-block;margin-top:10px;padding:5px 14px}

/* footer */
.site-footer{position:absolute;top:1058px;left:52px;width:607px;display:flex}
.foot-brand{width:118px;display:flex;flex-direction:column;align-items:flex-start;gap:5px}
.foot-col{font-size:6px;color:var(--muted);line-height:1.8}
.foot-col h5{font-size:6.5px;color:var(--ink);font-weight:600;margin-bottom:2px;letter-spacing:.3px}
.about{width:120px}
.newsletter{width:160px}
.newsletter .field{display:flex;width:120px;height:14px;border:1px solid var(--line);margin-top:6px}
.newsletter .field span{flex:1;font-size:5px;padding:3px}
.newsletter .field i{width:14px;background:var(--dark)}
.contact{flex:1}
.contact li{list-style:none;display:flex;gap:4px}
.contact svg{flex:none;margin-top:2px}
.bottom-bar{position:absolute;left:0;top:1168px;width:711px;height:32px;background:var(--bar);
  display:flex;align-items:center;justify-content:space-between;padding:0 52px;font-size:6px;color:#ddd}
.social{display:flex;gap:4px}
.social i{width:11px;height:11px;background:#777;display:block}
</style>
</head>
<body>
<div class="page">

<header class="site-header">
  <div class="brand"><span class="brand-dot"></span><span class="brand-name">The Velvet<br>Pathfinder</span></div>
  <nav class="main-nav">
    <span class="active">Home</span><span>How it works</span><span>Diamond Gallery</span><span>About</span><span>FAQs</span><span>Contact</span>
    <div class="auth"><span class="btn-sm">Sign in</span><span class="btn-sm fill">Sign up</span></div>
  </nav>
</header>

<section class="hero">
  <div class="hero-text">
    <div class="hero-kicker">Welcome to</div>
    <div class="hero-title">The Velvet Pathfinder</div>
    <div class="hero-sub">Beautiful Diamond Rings. All online. Starting from $5000</div>
    <span class="btn-dark">Find Now</span>
  </div>
  <div class="hero-photo" role="img" aria-label="Gold and diamond ring photograph"></div>
  <div class="hero-deco" role="img" aria-label="Faint antler decoration"></div>
  <span class="arrow left">&#8249;</span><span class="arrow right">&#8250;</span>
</section>

<section class="process">
  <h2 class="section-title">The Velvet Pathfinder's process</h2>
  <div class="steps">
    <svg width="711" height="90" viewBox="0 0 711 90" style="position:absolute;left:0;top:0">
      <g fill="none" stroke="#bbb" stroke-width="1">
        <line x1="186" y1="40" x2="268" y2="40" stroke-dasharray="2 3"/>
        <line x1="310" y1="40" x2="392" y2="40" stroke-dasharray="2 3"/>
        <line x1="434" y1="40" x2="516" y2="40" stroke-dasharray="2 3"/>
        <rect x="151" y="25" width="30" height="30" transform="rotate(45 166 40)"/>
        <rect x="274" y="25" width="30" height="30" transform="rotate(45 289 40)"/>
        <rect x="397" y="25" width="30" height="30" transform="rotate(45 412 40)"/>
        <rect x="525" y="25" width="30" height="30" transform="rotate(45 540 40)"/>
      </g>
      <g fill="none" stroke="#444" stroke-width="1.2">
        <circle cx="164" cy="38" r="5"/><line x1="168" y1="42" x2="172" y2="46"/>
        <rect x="283" y="32" width="12" height="15"/><line x1="286" y1="37" x2="292" y2="37"/><line x1="286" y1="41" x2="292" y2="41"/>
        <rect x="406" y="35" width="12" height="12"/><path d="M409 35 v-3 h6 v3"/>
        <path d="M534 40 l4 4 l8 -9"/>
      </g>
    </svg>
    <div class="step-caption" style="left:106px"><b>1</b>Search your diamond Ring</div>
    <div class="step-caption" style="left:229px"><b>2</b>Choose your favourite ring</div>
    <div class="step-caption" style="left:352px"><b>3</b>We'll shop for you</div>
    <div class="step-caption" style="left:480px"><b>4</b>You get your product easily</div>
  </div>
</section>

<section class="gallery">
  <h2 class="section-title">The Velvet Pathfinder's gallery</h2>
  <div class="grid">
    <div class="tile-photo bracelet" role="img" aria-label="Diamond tennis bracelet photograph"></div>
    <div class="info-tile">
      <h3>Diamond Ring</h3>
      <p>Hand-picked stones sourced from trusted jewellers, set in fine metal and checked for cut and clarity.</p>
      <span class="btn-line">View Product</span>
    </div>
    <div class="tile-photo emerald" role="img" aria-label="Emerald and diamond ring photograph"></div>
    <div class="tile-photo gold" role="img" aria-label="Gold diamond band photograph"></div>
  </div>
</section>

<section class="packages">
  <div class="pack-photo" role="img" aria-label="Scattered diamonds and jewellery photograph"></div>
  <div class="pack-card">
    <h4>Package 1</h4>
    <div class="price">$5000 <span>/ Ring</span></div>
    <p>Includes<br>Personal search across stores<br>Shortlist of matching rings<br>Secure ordering on your behalf</p>
    <span class="btn-dark">Buy Now</span>
  </div>
  <div class="pack-card">
    <h4>Package 2</h4>
    <div class="price">$5000 <span>/ Ring</span></div>
    <p>Includes<br>Personal search across stores<br>Shortlist of matching rings<br>Secure ordering on your behalf</p>
    <span class="btn-line">Buy Now</span>
  </div>
</section>

<footer class="site-footer">
  <div class="foot-brand"><span class="brand-dot"></span><span class="brand-name">The Velvet<br>Pathfinder</span></div>
  <div class="foot-col about">
    <h5>ABOUT US</h5>
    Diamond Gallery<br>How it works<br>About us<br>FAQs<br>Contact us
  </div>
  <div class="foot-col newsletter">
    <h5>NEWSLETTER</h5>
    Be first to receive our latest news, great<br>offers and new features directly to your<br>inbox.
    <div class="field"><span>Enter email address</span><i></i></div>
  </div>
  <div class="foot-col contact">
    <h5>CONTACT</h5>
    <ul>
      <li><svg width="6" height="7" viewBox="0 0 6 7"><path d="M3 7 C1 4 0 3 0 2 a3 2 0 0 1 6 0 c0 1 -1 2 -3 5z" fill="#888"/></svg>14 Harbour Lane, Unit 6, Riverside<br>City, State 2041, Country</li>
      <li><svg width="6" height="7" viewBox="0 0 6 7"><rect x="1" y="0" width="4" height="7" rx="1" fill="#888"/></svg>+11 5550 2741</li>
      <li><svg width="6" height="7" viewBox="0 0 6 7"><rect x="0" y="1" width="6" height="5" fill="none" stroke="#888"/></svg>hello@velvetpathfinder.com</li>
    </ul>
  </div>
</footer>

<div class="bottom-bar">
  <span>&copy; The Velvet Pathfinder. All Rights Reserved</span>
  <div class="social"><i></i><i></i></div>
</div>

</div>
</body>
</html>
```